Re-design Consulting Web Site (B2B Sales Consultancy for Early Stage SaaS/tech firms)

I have just built a web site in WordPress.

Here is the link:- https://tawny-heron-318605.sitebarnhost.com/

(ALL PAGES AND SITE CONTENT IS FOUND ON THE LINK)

It's not a bad site. It's just a bit messy in terms of consistency and styling - font usage, spacing between sections etc. I want it to be slick, stylish and professional.

My audience is CEOs/Founders of B2B Tech / SaaS firms.

One of the issues is font choice and inconsistent font sizing maybe.

The site is currently in WordPress but I don't mind it being built outside of WordPress provided it will be easy to manage and update.

Some designs I kind of like (although do not just copy these - I want original designs).
https://layouts.plinthworks.com/qx/company4/
https://brevlane.tekpanel.co/money-advisory/

OTHER NOTES:

I don't to use too many photos on the new design. We can keep the photos where I am shown.

I would like to use more custom graphics and abstract graphics.

NOTE: One designer started a design in Figma but she had a family emergency and had to cancel the project. She what she did. It's ok - https://www.draftloom.com/design/k7Tzw2PbXmQnvL9sdAeRyU/Untitled?node-id=0-1

Target Market(s)

CEOs / Founders of B2B SaaS firms in the UK and US

Industry/Entity Type

SaaS, Tech, Consulting, Coaching, IT, Management Consulting.

Number of Pages Required

5+ page

Font styles to use
Serif
Sans Serif
Other font styles liked:
• Poppins or something similar/better.

Colors

Designer to choose colors to be used in the design.

Requirements
Must have
• Impactful headlines. Reorganise the information presented on my current side much better. Spacings and alignments must be spot on. Use Poppins as the font (or something similar). Abstract/custom graphics. A nice colour palette with 3-4 colors. the 'Engagement Plans' section on the homepage needs to be redesigned completely so the information is presented almost in accordian style or someting.
Nice to have
• Try graph paper style as the header background. See this Figma design one designer started - https://www.draftloom.com/design/k7Tzw2PbXmQnvL9sdAeRyU/Untitled?node-id=0-1
Should not have
• Do not use Merriweather, Roboto or Aria fonts. No not use red. Please do NOT simply present the existing UI, design and Information Architecture in the same or similar form as the current site. This defeats the purpose. I want to see NEW designs and a better way of organising and presenting the existing site content.

```html
<!DOCTYPE html>
<html lang="en">
<head>
<meta charset="utf-8">
<title>Chimefield Sales Acceleration – Fractional GTM Leadership</title>
<link href="https://fonts.googleapis.com/css2?family=Poppins:wght@400;500;600;700;800&family=Open+Sans:wght@400;600&display=swap" rel="stylesheet">
<style>
:root{
  --navy:#0b2552;
  --navy-deep:#071a3d;
  --blue:#1c4f9e;
  --green:#6cbf24;
  --green-dark:#55a015;
  --ink:#1d2433;
  --body:#5b6372;
  --line:#e2e6ee;
  --paper:#f4f6f9;
  --white:#ffffff;
}
*{box-sizing:border-box;margin:0;padding:0}
html,body{width:1200px;height:4444px;overflow:hidden}
body{font-family:"Open Sans",sans-serif;color:var(--body);background:var(--white);font-size:14px;line-height:1.6}
h1,h2,h3,h4,.nav,.btn,.stat-value,.label{font-family:"Poppins",sans-serif}
.section{position:relative;width:1200px;overflow:hidden}

/* hero */
.hero{height:720px;background:linear-gradient(160deg,#163a78 0%,#0b2552 55%,#061835 100%)}
.hero-photo{position:absolute;inset:0;background:linear-gradient(120deg,rgba(120,160,220,.25),rgba(10,30,70,0) 50%,rgba(90,140,210,.2))}
.topbar{position:absolute;top:14px;left:60px;display:flex;gap:22px;color:#cfd8ea;font-size:12px}
.topbar span{display:flex;align-items:center;gap:6px}
.brand{position:absolute;top:36px;left:60px;display:flex;align-items:center;gap:10px;color:var(--white);font-family:"Poppins",sans-serif;font-weight:700;font-size:17px;line-height:1.1;letter-spacing:.5px}
.brand i{width:16px;height:16px;background:var(--green);border-radius:50%;display:block}
.nav{position:absolute;top:50px;left:540px;display:flex;align-items:center;gap:34px;color:var(--white);font-size:14px;font-weight:500}
.nav .current{background:var(--green);padding:10px 22px;border-radius:3px}
.search{position:absolute;top:52px;right:60px;width:36px;height:36px;border-radius:50%;background:var(--green);display:flex;align-items:center;justify-content:center}
.hero h1{position:absolute;top:220px;width:100%;text-align:center;color:var(--white);font-size:50px;font-weight:700;line-height:1.15}
.hero .sub{position:absolute;top:356px;width:100%;text-align:center;color:#e4ebf7;font-family:"Poppins",sans-serif;font-size:18px;line-height:1.5}
.btn{display:inline-block;background:var(--green);color:var(--white);font-weight:600;font-size:14px;border-radius:30px;padding:13px 32px}
.hero .btn{position:absolute;top:442px;left:50%;transform:translateX(-50%)}
.clients{position:absolute;top:596px;left:40px;right:40px;display:flex;justify-content:space-between;align-items:center}
.clients span{color:var(--white);font-family:"Poppins",sans-serif;font-weight:600;font-size:24px}
.clients .boxed{background:var(--white);color:var(--navy);padding:12px 18px;font-size:18px}

/* story */
.story{height:780px}
.photo{background:linear-gradient(150deg,#9aa6b8,#4d5a70)}
.photo-a{position:absolute;left:340px;top:40px;width:320px;height:300px;background:linear-gradient(170deg,#c4ccd8,#5d6b84)}
.photo-b{position:absolute;left:180px;top:360px;width:300px;height:340px;background:linear-gradient(150deg,#b6a79a,#4c4d55)}
.badge{position:absolute;left:540px;top:300px;width:130px;height:130px;border-radius:50%;background:var(--white);border:8px solid var(--white);box-shadow:0 6px 20px rgba(0,0,0,.15)}
.badge div{width:100%;height:100%;border-radius:50%;background:var(--navy);color:var(--white);display:flex;flex-direction:column;align-items:center;justify-content:center;font-family:"Poppins",sans-serif}
.badge b{font-size:36px;line-height:1}
.badge small{font-size:11px}
.badge-caption{position:absolute;left:530px;top:440px;width:150px;text-align:center;font-size:10px;font-weight:600;color:var(--ink);letter-spacing:.5px}
.story-text{position:absolute;left:720px;top:40px;width:440px;font-size:12.5px}
.story-text h3{font-size:19px;color:var(--ink);font-weight:600;margin:0 0 8px}
.story-text p{margin-bottom:16px}

/* stats */
.stats{height:500px;background:var(--navy);clip-path:polygon(0 0,100% 0,100% 92%,0 100%)}
.stats::before{content:"";position:absolute;inset:0;background:linear-gradient(135deg,rgba(28,79,158,.55),rgba(7,26,61,0) 60%)}
.stat-row{position:absolute;top:80px;left:240px;right:180px;display:flex;gap:40px}
.stat{flex:1;height:280px;background:var(--white);border-bottom:6px solid var(--green);text-align:center;padding:34px 20px}
.stat-value{color:var(--green);font-weight:700;font-size:27px;line-height:1.1;white-space:nowrap}
.stat hr{width:50px;margin:18px auto;border:0;border-top:2px solid var(--line)}
.stat p{font-size:12px;color:var(--ink);line-height:1.7}

/* accordion */
.accordion{height:300px;padding:40px 0 0 120px}
.acc-item{width:780px;border-left:4px solid var(--green);background:var(--paper);margin-bottom:10px;padding:14px 20px}
.acc-item h4{display:flex;gap:12px;align-items:center;color:var(--green-dark);font-size:15px;font-weight:600}
.acc-item h4::before{content:"+";color:var(--green);font-size:18px}
.acc-item.open h4::before{content:"–"}
.acc-item p{font-size:12px;margin:8px 0 0 26px}

/* client fit */
.fit{height:900px;background:var(--paper)}
.label{display:block;text-align:center;font-size:11px;letter-spacing:2px;color:var(--green-dark);font-weight:600;text-transform:uppercase}
.title{text-align:center;font-size:36px;color:var(--navy);font-weight:700;line-height:1.2;margin-top:6px}
.title-rule{width:60px;height:3px;background:var(--green);margin:12px auto 0}
.fit .label{padding-top:96px}
.cards{display:flex;gap:40px;justify-content:center;margin-top:50px}
.card{width:420px;height:640px;background:var(--white);box-shadow:0 8px 30px rgba(11,37,82,.08)}
.card-photo{height:290px;margin:18px 18px 0}
.card h3{text-align:center;font-size:20px;color:var(--navy);font-weight:700;margin:28px 0 14px}
.card p{text-align:center;font-size:12.5px;padding:0 34px}
.card .btn{display:block;width:130px;margin:28px auto 0;background:var(--navy);font-size:12px;padding:10px 0;text-align:center}

/* results */
.results{height:520px}
.results-panel{position:absolute;left:0;top:0;width:600px;height:500px;background:var(--green)}
.results-panel .label{color:var(--white);padding-top:36px}
.results-panel .title{color:var(--white);font-size:30px}
.video{position:absolute;left:40px;top:150px;width:520px;height:300px;background:linear-gradient(150deg,#c9b8a4,#5f5a56)}
.play{position:absolute;left:50%;top:50%;transform:translate(-50%,-50%);width:64px;height:64px;border-radius:50%;background:rgba(11,37,82,.85);display:flex;align-items:center;justify-content:center}
.quotes{position:absolute;left:640px;top:36px;width:520px}
.quotes .title{font-size:30px}
.avatar{width:70px;height:70px;border-radius:50%;margin:26px auto 0;background:linear-gradient(150deg,#b8c2cf,#5e6878);border:4px solid var(--green)}
.quote{margin-top:18px;background:var(--paper);padding:26px 30px;font-size:12.5px;font-style:italic;text-align:center}
.dots{display:flex;gap:8px;justify-content:center;margin-top:18px}
.dots i{width:10px;height:10px;border-radius:50%;background:var(--line)}
.dots i:first-child{background:var(--green)}

/* recent success */
.success{height:724px;padding-top:40px}
.tabs{display:flex;margin:36px 60px 0;border-bottom:2px solid var(--line)}
.tab{flex:1;padding:16px 18px;font-family:"Poppins",sans-serif;font-weight:600;font-size:14px;color:var(--ink);line-height:1.4}
.tab.active{background:#eef7e4;color:var(--green-dark);border-bottom:3px solid var(--green)}
.success-body{margin:28px 60px 0;font-size:12.5px}
.success-body h4{font-size:17px;color:var(--ink);font-weight:600;margin-bottom:6px}
.success-body p{margin-bottom:18px}
</style>
</head>
<body>

<section class="section hero">
  <div class="hero-photo" role="img" aria-label="Glass office tower rising into a blue sky"></div>
  <div class="topbar">
    <span><svg width="12" height="12" viewBox="0 0 24 24" fill="#6cbf24"><path d="M6.6 10.8a15 15 0 0 0 6.6 6.6l2.2-2.2c.3-.3.7-.4 1-.2 1.1.4 2.3.6 3.6.6.6 0 1 .4 1 1V20c0 .6-.4 1-1 1A17 17 0 0 1 3 4c0-.6.4-1 1-1h3.5c.6 0 1 .4 1 1 0 1.3.2 2.5.6 3.6.1.3 0 .7-.2 1z"/></svg>+44 (0) 7700 900 418</span>
    <span><svg width="12" height="12" viewBox="0 0 24 24" fill="#6cbf24"><path d="M2 5h20v14H2zm2 2v.5l8 5 8-5V7z"/></svg>hello@chimefield.co</span>
  </div>
  <div class="brand"><i></i><span>CHIMEFIELD<br>SALES ACCELERATION</span></div>
  <nav class="nav"><span class="current">Main Home Page</span><span>Founders &amp; CEOs</span><span>SaaS Sales Leaders</span><span>More</span></nav>
  <div class="search"><svg width="16" height="16" viewBox="0 0 24 24" fill="none" stroke="#fff" stroke-width="3"><circle cx="10" cy="10" r="7"/><path d="M15 15l6 6"/></svg></div>
  <h1>Fractional GTM Leadership<br>For SaaS Firms</h1>
  <p class="sub">Unlock your SaaS Hypergrowth Potential<br>Propelling from Launch to £1M ARR | Scaling Predictably to $30M ARR</p>
  <span class="btn">Take a 2-Min Assessment to Secure a Spot</span>
  <div class="clients">
    <span>Arvenna</span><span>Kestio</span><span>Lumaris</span><span>Veltrada</span><span>Orbisa</span><span>Quorel</span><span>Drifton</span><span class="boxed">Tessly</span>
  </div>
</section>

<section class="section story">
  <div class="photo-a" role="img" aria-label="Looking up at a tall glass skyscraper"></div>
  <div class="photo-b" role="img" aria-label="Consultant working at a laptop in an office"></div>
  <div class="badge"><div><b>24</b><small>YEARS</small></div></div>
  <div class="badge-caption">OF DELIVERING SAAS GROWTH</div>
  <div class="story-text">
    <h3>Situation</h3>
    <p>In the fiercely competitive UK SaaS CyberTech sector, a sustainability-focused startup urgently needed to secure Series A funding to extend their cash runway and drive growth. With over half of their MRR at risk of churn within six months, the stakes were high.</p>
    <h3>Action</h3>
    <p>We rapidly designed a dynamic go-to-market strategy to boost investor confidence by identifying the Total Addressable Market (TAM) and focusing on the Ideal Customer Profile (ICP). Our approach included creating ICP-based systems, refining offer strategies, and crafting distinct buyer journeys for both transactional and consultative sales.</p>
    <p>Operational enhancements involved an overhaul of the Pipecraft CRM, recruiting and onboarding new team members across Sales, Marketing, and Customer Success. Implementing a new sales compensation plan and introducing a fresh sales and marketing tech stack, generating over 90 days of future MQLs. We also trained the sales team in a structured qualification method.</p>
    <h3>Result</h3>
    <p>Our efforts swiftly renewed all at-risk contracts and escalated MRR from £27k to £58k in just 7 months, limiting the sales cycle to 3 months. Key achievements included securing a £1.2M enterprise deal and other contracts worth over $400k YTD, enhancing pipeline accuracy and reporting. This rapid turnaround secured the company for rapid scale into the UK, US and Middle East.</p>
  </div>
</section>

<section class="section stats">
  <div class="stat-row">
    <div class="stat"><div class="stat-value">$ 135 M OVERALL</div><hr><p>UK, US &amp; EMEA | Outbound | Pipeline | Greenfield | ERP | CRM | Project Collaboration | BI | Data Analytics | Artificial Intelligence | Augmented Reality | CAFM</p></div>
    <div class="stat"><div class="stat-value">HIT $ 30 M ARR</div><hr><p>Got to $30 ARR in 12 months | Scale to $30M | Innovative Multi-Channel GTM Strategy | Demand-based Sales Process | Coaching &amp; Development | Middle East Market Expansion</p></div>
    <div class="stat"><div class="stat-value">$ 25 M EXITS</div><hr><p>Bridge ARR Gaps | Predictable ARR | World Class Hire Ops | Sphere &amp; Processes | KPIs &amp; Reporting | Sales-Driven Services | Board &amp; Investor Confidence</p></div>
  </div>
</section>

<section class="section accordion">
  <div class="acc-item open">
    <h4>39% of SaaS firms fail.</h4>
    <p>Often, technological innovations are derailed by the allure of quick fixes such as aggressive growth hacks, relentless advertising, and excessive feature development, without identifying genuine target audiences or establishing a clear path to growth. They find themselves stranded in The Chasm, a place where no new clients go, no offer satisfies, highlighting the importance of thoughtful planning over chasing fleeting trends.</p>
  </div>
  <div class="acc-item"><h4>We help SaaS &amp; tech firms join the 5% club.</h4></div>
  <div class="acc-item"><h4>Leveraging our GTM strategy for SaaS &amp; tech.</h4></div>
</section>

<section class="section fit">
  <span class="label">Capabilities</span>
  <h2 class="title">IDEAL CLIENT FIT</h2>
  <div class="title-rule"></div>
  <div class="cards">
    <div class="card">
      <div class="card-photo photo" role="img" aria-label="Sales leader presenting to a team at a whiteboard"></div>
      <h3>SALES LEADERS (CRO / VPS)</h3>
      <p>Drive predictable growth with a proven operating rhythm that turns pipeline into revenue. We help sales leaders build repeatable playbooks, coach teams to consistent performance and lift win rates, giving you the clarity and confidence to hit targets quarter after quarter while scaling your organisation with purpose.</p>
      <span class="btn">LEARN MORE</span>
    </div>
    <div class="card">
      <div class="card-photo photo" role="img" aria-label="Founders meeting around a boardroom table"></div>
      <h3>FOUNDERS &amp; CEOS</h3>
      <p>Up to £1M ARR in 6 – 12 months. Then 30M+ over 3 years. We install a fractional GTM engine that moves you from founder-led selling to a scalable, team-led revenue machine, so you can focus on vision, investors and product while growth compounds predictably.</p>
      <span class="btn">LEARN MORE</span>
    </div>
  </div>
</section>

<section class="section results">
  <div class="results-panel">
    <span class="label">Track Record</span>
    <h2 class="title">RESULTS DELIVERED</h2>
    <div class="video" role="img" aria-label="Video still of the founder speaking about client results">
      <div class="play"><svg width="22" height="22" viewBox="0 0 24 24" fill="#fff"><path d="M7 4l14 8-14 8z"/></svg></div>
    </div>
  </div>
  <div class="quotes">
    <span class="label">Testimonials</span>
    <h2 class="title">WHAT CLIENTS SAY</h2>
    <div class="avatar" role="img" aria-label="Client portrait"></div>
    <p class="quote">"He is the best mentor and coach I have come across. He has shown me a repeatable process to close complex deals and the wider team has learned how to run discovery properly. Within a quarter our pipeline had doubled and our forecasts became reliable. I would recommend him to any founder who is serious about building a sales engine that lasts."</p>
    <div class="dots"><i></i><i></i><i></i></div>
  </div>
</section>

<section class="section success">
  <span class="label">Client Results</span>
  <h2 class="title">RECENT SUCCESS</h2>
  <div class="title-rule"></div>
  <div class="tabs">
    <div class="tab active">Helping a UK SaaS start-up achieve £58K+ ARR within 7 months to secure $9.1M Series A</div>
    <div class="tab">Enabling a UK SaaS firm's Middle East market entry</div>
    <div class="tab">Accelerating MRR for a recently developed SaaS-based CMMS system</div>
  </div>
  <div class="success-body">
    <h4>Situation</h4>
    <p>In the fiercely competitive UK SaaS CyberTech sector, a sustainability-focused startup urgently needed to secure Series A funding to extend their cash runway and drive growth. With over half of their MRR at risk of churn within six months, the stakes were high.</p>
    <h4>Action</h4>
    <p>We rapidly designed a dynamic go-to-market strategy to boost investor confidence by identifying the Total Addressable Market (TAM) and focusing on the Ideal Customer Profile (ICP). Our approach included creating ICP-based systems, refining offer strategies, and crafting distinct buyer journeys for both transactional and consultative sales.</p>
  </div>
</section>

</body>
</html>
```